Meditation for IVF and infertility

I need a flyer inviting IVF patients to join my Meditation class, I would like to offer free meditation to ivf women and for couples this class is free every Thursday night at 5 pm
2465 west halloran blvd suite K Santa Barbara Ca 93274
larkvale-meditation.com for more details

```html
<!DOCTYPE html>
<html lang="en">
<head>
<meta charset="utf-8">
<title>Meditation for Infertility &amp; IVF</title>
<link href="https://fonts.googleapis.com/css2?family=Zilla+Slab:wght@300;400;500;600;700&family=Lato:wght@400;700;900&family=Lora:wght@400;700&display=swap" rel="stylesheet">
<style>
  :root {
    --ink: #3a3b3b;
    --ink-deep: #111111;
    --stone: #d3cac8;
    --blush: #efdcd8;
    --blush-text: #f0d9d3;
    --paper: #f8f8f7;
    --white: #ffffff;
  }
  * { margin: 0; padding: 0; box-sizing: border-box; }
  html, body { width: 1200px; height: 846px; overflow: hidden; background: var(--paper); }
  .flyer { position: relative; width: 1200px; height: 846px; overflow: hidden; background: var(--paper); }

  .hero-photo {
    position: absolute; inset: 0;
    background:
      radial-gradient(ellipse 260px 380px at 300px 520px, #c9c9c9 0%, rgba(220,220,220,0.6) 55%, rgba(248,248,247,0) 100%),
      linear-gradient(180deg, #f8f8f7 0%, #f3f3f2 70%, #e6e3e0 85%, #ebe9e6 100%);
  }

  .panels { position: absolute; left: 0; top: 0; }

  .headline { position: absolute; left: 0; top: 0; font-weight: 400; }
  .title {
    position: absolute; left: 62px; white-space: nowrap;
    font-family: "Zilla Slab", serif; font-weight: 400;
    line-height: 1; color: var(--ink);
  }
  .title--top { top: 283px; font-size: 180px; letter-spacing: 3px; }
  .title--bottom { top: 437px; font-size: 118px; letter-spacing: 3px; }

  .with-line {
    position: absolute; left: 62px; top: 562px; white-space: nowrap;
    font-family: "Lato", sans-serif; font-weight: 900;
    font-size: 32px; line-height: 1; letter-spacing: 4px; color: var(--ink-deep);
  }
  .highlight { background: var(--blush); padding: 2px 2px 4px 2px; }

  .subtitle {
    position: absolute; left: 62px; white-space: nowrap;
    font-family: "Zilla Slab", serif; font-weight: 300;
    font-size: 77px; line-height: 1; color: var(--ink);
  }
  .subtitle--one { top: 619px; }
  .subtitle--two { top: 708px; }

  .intro {
    position: absolute; left: 697px; top: 60px; width: 450px;
    font-family: "Zilla Slab", serif; font-weight: 500;
    font-size: 25px; line-height: 30.5px; letter-spacing: 2.6px;
    color: var(--ink); text-transform: uppercase;
  }
  .intro strong { font-weight: 700; }
  .intro .name-tag { background: var(--blush); color: var(--white); padding: 0 2px; }

  .day {
    position: absolute; left: 621px; width: 560px; top: 328px; text-align: center;
    font-family: "Zilla Slab", serif; font-weight: 300;
    font-size: 66px; line-height: 1; letter-spacing: 4px; color: var(--ink);
  }
  .time {
    position: absolute; left: 621px; width: 560px; top: 402px; text-align: center;
    font-family: "Lato", sans-serif; font-weight: 400;
    font-size: 38px; line-height: 1; letter-spacing: 1px; color: var(--ink-deep);
  }

  .brand-name {
    position: absolute; left: 812px; width: 180px; top: 530px; text-align: center;
    font-family: "Zilla Slab", serif; font-weight: 500; color: var(--white);
    font-size: 24px; line-height: 1.05;
  }

  .contact {
    position: absolute; left: 621px; width: 560px; text-align: center;
    font-family: "Lora", serif; line-height: 1; white-space: nowrap;
  }
  .contact--address { top: 662px; font-size: 16px; color: var(--white); }
  .contact--dot { top: 686px; font-size: 16px; color: var(--white); }
  .contact--phone { top: 715px; font-size: 19px; color: var(--blush-text); }
  .contact--web { top: 748px; font-size: 19px; font-weight: 700; color: var(--blush-text); }
</style>
</head>
<body>
<main class="flyer">
  <div class="hero-photo" role="img" aria-label="Soft faded photograph of a woman seated cross-legged in a twisting meditation pose, eyes closed"></div>

  <svg class="panels" width="1200" height="846" viewBox="0 0 1200 846" aria-hidden="true">
    <rect class="panel-stone" x="621" y="0" width="560" height="299" fill="var(--stone)"/>
    <rect class="panel-blush" x="621" y="302" width="560" height="230" fill="var(--blush)"/>
    <path class="panel-ink-outline" d="M621 534 H1181 V540 A280 264 0 0 1 621 540 Z" fill="none" stroke="var(--white)" stroke-width="2"/>
    <path class="panel-ink" d="M621 534 H1181 V538 A280 264 0 0 1 621 538 Z" fill="var(--ink)"/>
    <circle class="brand-ring" cx="901" cy="550" r="90" fill="var(--ink)" stroke="var(--white)" stroke-width="2.5"/>
  </svg>

  <h1 class="headline">
    <span class="title title--top">MEDI</span>
    <span class="title title--bottom">TATION</span>
  </h1>
  <p class="with-line">WITH <span class="highlight">MARA QUILL</span></p>
  <p class="subtitle subtitle--one">for Infertility</p>
  <p class="subtitle subtitle--two">&amp; IVF.</p>

  <p class="intro"><strong>Join</strong> instructor <span class="name-tag">Mara Quill</span> for a guided meditation session, for all IVF women &amp; couples regardless of where you are in your fertility journey.</p>

  <p class="day">THURSDAY</p>
  <p class="time">5:00 PM</p>

  <p class="brand-name">Larkvale<br>Meditation</p>

  <p class="contact contact--address">2465 W Halloran Blvd Suite K, Santa Barbara, CA 93274</p>
  <p class="contact contact--dot">&bull;</p>
  <p class="contact contact--phone">phone: (707) 555-0148</p>
  <p class="contact contact--web">larkvale-meditation.com</p>
</main>
</body>
</html>
```